Harborline Security and Surveillance Business Card

Business Card Design - Company Name:Freedom Security and SurveillanceWe are a Security Systems Integrator Specializing in Security Systems/ Video Surveillance and Access Control. Our areas of expertise are:Security SystemsVideo SurveillanceAccess ControlFire Alarm SystemsNetwork CablingCellular BoostersMy input is the Front of the Card is: logo, name of Business, My Name, Phone Number, and email.Rear of Card is the 6 areas of expertise, I just dont want the front to be very busy.
Name: Dale Varnik
Title: President
Email: dale@harborlinesecsys.example
website: harborlinesecsys.example

```html
<!DOCTYPE html>
<html lang="en">
<head>
<meta charset="utf-8">
<title>Harborline Security and Surveillance Business Card</title>
<link href="https://fonts.googleapis.com/css2?family=Arimo:wght@400;700&display=swap" rel="stylesheet">
<style>
  :root {
    --backdrop: #9a9a9a;
    --card-light: #f1f4fc;
    --card-mid: #e3e8f6;
    --card-edge: #1b5fc4;
    --brand-blue: #1a5fc8;
    --text-blue: #1c56b8;
    --ink: #111111;
    --band-grey: #c6cbd6;
    --icon-grey: #8e9096;
    --mark-tint: #c9d6f0;
  }
  * { box-sizing: border-box; margin: 0; padding: 0; }
  html, body { width: 1200px; height: 1000px; overflow: hidden; }
  body {
    background: var(--backdrop);
    font-family: "Arimo", Arial, sans-serif;
    position: relative;
  }
  .card {
    position: absolute;
    left: 224px;
    width: 752px;
    height: 429px;
    background: radial-gradient(ellipse at 55% 45%, var(--card-light) 0%, var(--card-mid) 100%);
    border: 3px solid var(--card-edge);
    border-radius: 46px 22px 22px 22px;
    overflow: hidden;
  }
  .card--front { top: 18px; }
  .card--back { top: 502px; }

  .company-name {
    position: absolute;
    color: var(--brand-blue);
    font-weight: 700;
    text-transform: uppercase;
    line-height: 1;
    white-space: nowrap;
  }
  .company-name__main { display: block; }
  .company-name__sub { display: block; }

  .card--front .company-name { left: 36px; top: 50px; width: 680px; text-align: center; }
  .card--front .company-name__main { font-size: 50px; letter-spacing: 3px; }
  .card--front .company-name__sub { font-size: 19px; letter-spacing: 7px; margin-top: 4px; }

  .name-band {
    position: absolute;
    left: 0; top: 148px;
    width: 264px; height: 66px;
    background: var(--band-grey);
    clip-path: polygon(0 0, 100% 0, 87% 100%, 0 100%);
  }
  .person { position: absolute; left: 31px; top: 150px; white-space: nowrap; }
  .person__name { font-size: 32px; color: var(--text-blue); line-height: 1.05; }
  .person__title { font-size: 18px; color: var(--ink); margin-top: 2px; }

  .contact { position: absolute; left: 36px; list-style: none; }
  .contact--phone { top: 288px; }
  .contact--email { top: 332px; }
  .contact li { display: flex; align-items: center; gap: 16px; font-size: 17px; color: var(--text-blue); white-space: nowrap; }
  .contact svg { width: 28px; height: 28px; flex: none; }

  .brand-square { position: absolute; background: var(--mark-tint); }
  .card--front .brand-square { left: 476px; top: 150px; width: 250px; height: 250px; border-radius: 50%; }

  .card--back .brand-square { left: 20px; top: 103px; width: 100px; height: 100px; background: var(--brand-blue); }
  .card--back .company-name { left: 148px; top: 118px; }
  .card--back .company-name__main { font-size: 45px; letter-spacing: 2.5px; }
  .card--back .company-name__sub { font-size: 20px; letter-spacing: 22px; margin-top: 9px; }

  .expertise__label {
    position: absolute; left: 0; top: 235px; width: 100%;
    text-align: center; font-size: 12px; color: var(--ink);
  }
  .expertise__panel {
    position: absolute; left: 4px; top: 255px;
    width: 740px; height: 70px;
    background: var(--band-grey);
    border-radius: 12px;
    display: grid;
    grid-template-columns: 258px 256px 226px;
    grid-template-rows: 31px 31px;
    padding-top: 12px;
    font-size: 18.5px; color: var(--text-blue);
    text-align: center; list-style: none;
    white-space: nowrap;
  }
  .website {
    position: absolute; left: 0; top: 399px; width: 100%;
    text-align: center; font-size: 17px; color: var(--text-blue);
    text-decoration: underline;
  }
</style>
</head>
<body>

<section class="card card--front" aria-label="Card front">
  <h1 class="company-name">
    <span class="company-name__main">Harborline Security</span>
    <span class="company-name__sub">and Surveillance</span>
  </h1>
  <div class="name-band"></div>
  <div class="person">
    <p class="person__name">DALE VARNIK</p>
    <p class="person__title">PRESIDENT</p>
  </div>
  <ul class="contact contact--phone">
    <li>
      <svg viewBox="0 0 24 24" aria-hidden="true"><path fill="var(--icon-grey)" d="M6.6 2.5c.6-.3 1.3-.1 1.6.5l1.7 3.3c.3.6.1 1.2-.4 1.6l-1.3 1c.8 2.2 2.3 4.4 4.3 6.1l1.4-.9c.5-.4 1.200-.3 1.6.2l2.3 2.9c.4.5.3 1.2-.2 1.7l-1.6 1.4c-.8.7-2 .8-2.9.2C8 17.7 4.6 12 4.1 6.2c-.1-1.1.5-2.2 1.5-2.8z"/></svg>
      <span>1234567890</span>
    </li>
  </ul>
  <ul class="contact contact--email">
    <li>
      <svg viewBox="0 0 24 24" aria-hidden="true"><rect x="2.5" y="5" width="19" height="14" fill="none" stroke="var(--icon-grey)" stroke-width="1.8"/><path d="M2.5 5l9.5 8 9.5-8M2.5 19l7-6.5M21.5 19l-7-6.5" fill="none" stroke="var(--icon-grey)" stroke-width="1.8"/></svg>
      <span>dale@harborlinesecsys.example</span>
    </li>
  </ul>
  <div class="brand-square" aria-hidden="true"></div>
</section>

<section class="card card--back" aria-label="Card back">
  <div class="brand-square" aria-hidden="true"></div>
  <h2 class="company-name">
    <span class="company-name__main">Harborline Security</span>
    <span class="company-name__sub">and Surveillance</span>
  </h2>
  <p class="expertise__label">EXPERTISE IN</p>
  <ul class="expertise__panel">
    <li>SECURITY SYSTEMS VIDEO</li>
    <li>SURVEILLANCE ACCESS</li>
    <li>CONTROL FIRE ALARM</li>
    <li>SYSTEMS NETWORK</li>
    <li>CABLING CELLULAR</li>
    <li>BOOSTERS</li>
  </ul>
  <p class="website">harborlinesecsys.example</p>
</section>

</body>
</html>
```